New business card for our new logo

I have a brand new, existing logo. Now I need it on a new business card. The new card should include the following:

English language training
Translations
Interpreting Services (remote and in-person)

Target Market(s)

We are targeting international companies with foreign investment in the United States as well as domestic companies, medical offices, law offices, and non-profits that have non-native English speakers as their clients.

Contact Information for Business Card

Delia Brancombe, President
418 Garrow St.
Indianapolis, IN 46203
(317) 548-3162
info@tallpinewordworks.com
www.tallpinewordworks.com

Font styles to use
Sans Serif

Colors
0392cd
3176b5
abd036
9bcb3b
f04a50
f78f20

Requirements
Must have
• It must include our logo and business card details
Nice to have
• I would like to see a layout that is uncluttered and conveys trust and dependability, as well as the feelings of being friendly and approachable.

It would be nice to have icons for English language training, translating, and interpreting.
Should not have
• No pink, yellow, or purple

```html
<!DOCTYPE html>
<html lang="en">
<head>
<meta charset="utf-8">
<title>Tall Pine Wordworks – Business Card</title>
<link href="https://fonts.googleapis.com/css2?family=Lato:wght@400;700;900&display=swap" rel="stylesheet">
<style>
  :root {
    --brand-blue: #3b6ab3;
    --brand-blue-dark: #2f5aa3;
    --line-blue: #9db4dc;
    --ink-grey: #6d6f73;
    --paper: #ffffff;
    --backdrop: #e9ebee;
    --icon-tint: #5d86c6;
  }
  * { margin: 0; padding: 0; box-sizing: border-box; }
  html, body { width: 1200px; height: 900px; overflow: hidden; }
  body {
    background: var(--backdrop);
    font-family: "Lato", sans-serif;
    position: relative;
  }
  .card {
    position: absolute;
    left: 250px;
    width: 700px;
    height: 400px;
    border-radius: 34px;
    box-shadow: 0 6px 18px rgba(0,0,0,0.12);
    overflow: hidden;
  }
  .card--back { top: 40px; background: var(--brand-blue); color: var(--paper); }
  .card--front { top: 460px; background: var(--paper); }

  /* brand lockup */
  .brand { position: absolute; display: flex; align-items: center; gap: 18px; }
  .brand__dot { border-radius: 50%; flex: none; }
  .brand__name {
    font-family: "Lato", sans-serif;
    font-weight: 700;
    line-height: 1.02;
  }
  .card--back .brand { left: 210px; top: 70px; }
  .card--back .brand__dot { width: 96px; height: 96px; background: var(--paper); }
  .card--back .brand__name { font-size: 34px; color: var(--paper); }

  .card--front .brand { right: 70px; top: 52px; }
  .card--front .brand__dot { width: 100px; height: 100px; background: var(--brand-blue); }
  .card--front .brand__name { font-size: 34px; color: var(--brand-blue); }

  /* services */
  .services {
    position: absolute; left: 40px; right: 40px; bottom: 52px;
    display: flex; justify-content: space-around; align-items: flex-start;
  }
  .service { width: 190px; text-align: center; }
  .service__icon {
    width: 64px; height: 56px; margin: 0 auto 14px;
    border-radius: 8px;
    background: linear-gradient(160deg, #ffffff 0%, #d7e2f3 100%);
    opacity: 0.9;
  }
  .service__label { font-size: 18px; line-height: 1.2; }

  /* front details */
  .rule { position: absolute; height: 1.5px; background: var(--line-blue); }
  .rule--top { left: 40px; right: 40px; top: 186px; }
  .rule--mid { left: 40px; width: 270px; top: 290px; }

  .person { position: absolute; left: 48px; top: 214px; }
  .person__name { font-size: 36px; font-weight: 900; color: var(--brand-blue); line-height: 1; }
  .person__title { font-size: 19px; color: var(--ink-grey); margin-top: 8px; }

  .address {
    position: absolute; right: 56px; top: 206px;
    text-align: right; font-size: 18px; line-height: 1.3; color: var(--ink-grey);
  }

  .contacts { position: absolute; left: 48px; top: 302px; list-style: none; }
  .contacts li {
    display: flex; align-items: center; gap: 12px;
    font-size: 17px; color: var(--ink-grey); height: 28px;
  }
  .contacts svg { width: 18px; height: 18px; flex: none; }
</style>
</head>
<body>

<section class="card card--back" aria-label="Card back">
  <div class="brand">
    <span class="brand__dot"></span>
    <span class="brand__name">Tall Pine<br>Wordworks</span>
  </div>
  <div class="services">
    <div class="service">
      <div class="service__icon" role="img" aria-label="Icon of a teacher at a board for English language training"></div>
      <p class="service__label">English language<br>training</p>
    </div>
    <div class="service">
      <div class="service__icon" role="img" aria-label="Icon of two language cards with exchange arrows for translations"></div>
      <p class="service__label">Translations</p>
    </div>
    <div class="service">
      <div class="service__icon" role="img" aria-label="Icon of people in conversation for interpreting services"></div>
      <p class="service__label">Interpreting Services</p>
    </div>
  </div>
</section>

<section class="card card--front" aria-label="Card front">
  <div class="brand">
    <span class="brand__dot"></span>
    <span class="brand__name">Tall Pine<br>Wordworks</span>
  </div>

  <div class="rule rule--top"></div>

  <div class="person">
    <p class="person__name">Delia Brancombe</p>
    <p class="person__title">President</p>
  </div>

  <address class="address" style="font-style:normal">
    418 Garrow St.<br>Indianapolis, IN 46203
  </address>

  <div class="rule rule--mid"></div>

  <ul class="contacts">
    <li>
      <svg viewBox="0 0 24 24" aria-hidden="true"><path fill="#3b6ab3" d="M6.6 10.8a15 15 0 0 0 6.6 6.6l2.2-2.2a1 1 0 0 1 1-.25 11.4 11.4 0 0 0 3.6.57 1 1 0 0 1 1 1V20a1 1 0 0 1-1 1A17 17 0 0 1 3 4a1 1 0 0 1 1-1h3.5a1 1 0 0 1 1 1c0 1.25.2 2.45.57 3.57a1 1 0 0 1-.25 1z"/></svg>
      (317) 548-3162
    </li>
    <li>
      <svg viewBox="0 0 24 24" aria-hidden="true"><rect x="2" y="5" width="20" height="14" rx="2" fill="#3b6ab3"/><path d="M3 6l9 7 9-7" fill="none" stroke="#fff" stroke-width="1.6"/></svg>
      info@tallpinewordworks.com
    </li>
    <li>
      <svg viewBox="0 0 24 24" aria-hidden="true"><circle cx="12" cy="12" r="10" fill="#3b6ab3"/><g fill="none" stroke="#fff" stroke-width="1.2"><ellipse cx="12" cy="12" rx="4" ry="10"/><path d="M2 12h20M4 7h16M4 17h16"/></g></svg>
      www.tallpinewordworks.com
    </li>
  </ul>
</section>

</body>
</html>
```